Business Card for New Greek Restaurant

Looking for a Business card for a new Greek Restaurant that's focus is on Take out and Delivery & catering.

Also to outline the contact information for the restaurant.
Does not require a name or title of a specific person (Just general business card)
Phone (519) 372-FETA (3382)
Email : info@bluefigkitchen.ca
Website : www.bluefigkitchen.ca

Facebook/Instagram/Twitter Icons to Follow us as well.

TAKEOUT * DELIVERY* CATERING

Target Market(s)

Woman Age 25-44

Industry/Entity Type

Greek Restaurant

Contact Information for Business Card

Card is to have the general contact information for the business as well as outline our Take Out and Catering Services. Existing Logo attached and to be incorporated into the design.

Font styles to use
Sans Serif

Colors

Designer to choose colors to be used in the design.

Requirements
Must have
• Restaurant Contact Information :
• Phone (519) 372-FETA (3382)
• Email : info@bluefigkitchen.ca
• Website : www.bluefigkitchen.ca
• Highlight Takeout, Catering, Delivery
• Business Address :
• Marlow Crossing
• 27 Hollister Rd., Unit 6
• Breslau ON
• N0B 2K4
Nice to have
• Modern Feel to promote TakeOut and Catering Services.
Should not have
• No Specific Title or Contact Person (Generic Business Card for Restaurant)

```html
<!DOCTYPE html>
<html lang="en">
<head>
<meta charset="utf-8">
<title>Blue Fig Kitchen – Business Card</title>
<link href="https://fonts.googleapis.com/css2?family=Dosis:wght@600;700&family=Roboto:wght@400;500;700&display=swap" rel="stylesheet">
<style>
  :root {
    --stage: #d9d9d9;
    --brown: #6a3421;
    --brown-deep: #4f2415;
    --brown-text: #6b3a28;
    --orange: #f68b1f;
    --white: #ffffff;
    --cream: #f9f1e3;
    --cream-band: #f0d9a8;
    --sky: #1bb1e3;
    --photo-warm: #8a5a3a;
    --photo-dark: #3a2417;
  }
  * { margin: 0; padding: 0; box-sizing: border-box; }
  html, body {
    width: 1200px; height: 1000px; overflow: hidden;
    background: var(--stage);
  }
  .stage { position: relative; width: 1200px; height: 1000px; }
  .card {
    position: absolute; left: 270px; width: 662px; height: 378px;
    overflow: hidden;
  }
  .card--front { top: 108px; background: var(--brown); }
  .card--back { top: 521px; background: var(--cream); }

  .front-art { position: absolute; inset: 0; }
  .front-brand {
    position: absolute; left: 30px; top: 38px; width: 180px;
    font-family: "Dosis", sans-serif; font-weight: 700;
    color: var(--white); font-size: 30px; line-height: 1;
    letter-spacing: 1px; text-align: center;
  }
  .services {
    position: absolute; left: 340px; top: 82px; width: 300px;
    font-family: "Dosis", sans-serif; font-weight: 700;
    font-size: 56px; line-height: 72px; color: var(--orange);
  }
  .services .line { display: block; }
  .services .line--1 { padding-left: 32px; }
  .services .line--2 { padding-left: 62px; }
  .services .line--3 { padding-left: 47px; }
  .services .joiner { color: var(--white); }

  .back-logo {
    position: absolute; left: 247px; top: 41px;
    width: 166px; height: 166px; border-radius: 50%;
    background: var(--sky);
    display: flex; align-items: center; justify-content: center;
    text-align: center;
    font-family: "Roboto", sans-serif; font-weight: 700;
    color: var(--white); font-size: 24px; line-height: 1.15; letter-spacing: 1px;
  }
  .phone {
    position: absolute; left: 0; right: 0; top: 242px;
    display: flex; justify-content: center; align-items: center; gap: 10px;
    font-family: "Roboto", sans-serif; font-weight: 500;
    font-size: 42px; color: var(--brown-text);
  }
  .phone svg { width: 44px; height: 36px; }
  .web {
    position: absolute; left: 0; right: 0; top: 318px;
    text-align: center;
    font-family: "Roboto", sans-serif; font-weight: 400;
    font-size: 23px; color: var(--brown-text);
  }
  .web .sep { margin: 0 12px; }
</style>
</head>
<body>
<div class="stage">

  <section class="card card--front">
    <svg class="front-art" width="662" height="378" viewBox="0 0 662 378">
      <defs>
        <linearGradient id="brownFill" x1="0" y1="0" x2="1" y2="1">
          <stop offset="0" stop-color="#7a3d26"/>
          <stop offset="1" stop-color="#5a2a19"/>
        </linearGradient>
        <radialGradient id="photoFill" cx="0.45" cy="0.55" r="0.75">
          <stop offset="0" stop-color="#a87450"/>
          <stop offset="0.55" stop-color="#7a4b30"/>
          <stop offset="1" stop-color="#3a2417"/>
        </radialGradient>
      </defs>
      <rect class="card-ground" width="662" height="378" fill="url(#brownFill)"/>
      <path class="cream-band" d="M0 0 H290 Q400 180 248 378 H0 Z" fill="var(--cream-band)"/>
      <path class="food-photo" role="img" aria-label="Close-up photo of grilled souvlaki skewers"
            d="M0 0 H272 Q382 180 232 378 H0 Z" fill="url(#photoFill)"/>
    </svg>
    <div class="front-brand">BLUE FIG KITCHEN</div>
    <h1 class="services">
      <span class="line line--1">Takeout <span class="joiner">and</span></span>
      <span class="line line--2">Delivery</span>
      <span class="line line--3"><span class="joiner">&amp;</span> Catering</span>
    </h1>
  </section>

  <section class="card card--back">
    <div class="back-logo">BLUE FIG<br>KITCHEN</div>
    <p class="phone">
      <svg viewBox="0 0 44 36" aria-hidden="true">
        <path d="M2 12 Q2 3 22 3 Q42 3 42 12 L42 15 L33 15 L33 10 L11 10 L11 15 L2 15 Z" fill="var(--brown-text)"/>
        <path d="M9 17 L14 12 L30 12 L35 17 L39 32 Q39 34 37 34 L7 34 Q5 34 5 32 Z" fill="var(--brown-text)"/>
        <g fill="var(--cream)">
          <rect x="15" y="19" width="3" height="3"/><rect x="20.5" y="19" width="3" height="3"/><rect x="26" y="19" width="3" height="3"/>
          <rect x="15" y="24" width="3" height="3"/><rect x="20.5" y="24" width="3" height="3"/><rect x="26" y="24" width="3" height="3"/>
          <rect x="15" y="29" width="3" height="3"/><rect x="20.5" y="29" width="3" height="3"/><rect x="26" y="29" width="3" height="3"/>
        </g>
      </svg>
      <span>(519) 372-FETA (3382)</span>
    </p>
    <p class="web">info@bluefigkitchen.ca<span class="sep">|</span>www.bluefigkitchen.ca</p>
  </section>

</div>
</body>
</html>
```